Home Page Design (+50 More Pages To Winning Designer!)

We have a 50+ page website, but we're starting with the home page. The winning designer will get all 50+ pages to design as a 2nd project, so make sure you do your best!

Quorvel is in the private jet industry and needs a re-designed website.

We have created the structure for the website and content inside of Sketvo.io (THESE ARE ONLY ROUGH A.I. GENERATED WIREFRAMES AND DO NOT NEED TO BE FOLLOWED EXACTLY) - https://www.sketvo.io/app/project/P482915_kRmQzWvLpA-TTdoNeHfx83QZaplR77wqcyhtkLm5Hu2

Take the content from the 'Home Page' under the 'Wireframe' tab on the Sketvo.io link above, but feel free to re-design the page in a better way as these are only A.I. generated wireframes.

We want a DARK theme.... High quality, luxurious feel, greyscale colors. Attached is a brand guideline (BUT THIS IS NOT A 100% BRAND GUIDELINE, YOU CAN CHANGE COLORS AND FONTS AND MAKE CHANGES IF YOU HAVE BETTER IDEAS) and attached is our logo. We are also attaching some examples of other apps and websites to give you a guideline of what we're looking for for this design project.

The final design MUST communicate luxury using high-quality imagery of large cabin luxurious private jets.

ENTRIES THAT DO NOT FOLLOW THE PROJECT BRIEF WILL BE AUTOMATICALLY DISCARDED. FOLLOW THE INSTRUCTIONS!

Industry/Entity Type

Travel

Number of Pages Required

1 page

Font styles to use
Sans Serif

Colors

Designer to choose colors to be used in the design.

Requirements
Must have
• Follow wireframe and use content in wireframe (see Sketvo.io link)

```html
<!DOCTYPE html>
<html lang="en">
<head>
<meta charset="utf-8">
<title>Quorvel — Luxury Private Jet Travel</title>
<link href="https://fonts.googleapis.com/css2?family=Heebo:wght@300;400;500;600&display=swap" rel="stylesheet">
<style>
:root{
  --ink:#111;
  --black:#0d0d0d;
  --char:#1c1c1c;
  --dark:#2a2a2a;
  --band:#3a3a3a;
  --mid:#5a5a5a;
  --grey:#8a8a8a;
  --light:#c9c9c9;
  --paper:#f4f4f4;
  --white:#fff;
  --line:rgba(255,255,255,.55);
}
*{box-sizing:border-box;margin:0;padding:0}
html,body{width:1200px;height:5000px;overflow:hidden}
body{font-family:"Heebo",sans-serif;color:var(--white);background:var(--black);position:relative}
section,header,footer{position:absolute;left:0;width:1200px;overflow:hidden}
.abs{position:absolute}
.photo{position:absolute}
h1,h2,h3{font-weight:300;letter-spacing:.2px}
.btn{position:absolute;height:34px;display:flex;align-items:center;justify-content:center;font-size:10px;letter-spacing:1.4px;font-weight:500;text-transform:uppercase}
.btn-light{background:var(--white);color:var(--ink)}
.btn-ghost{border:1px solid var(--line);color:var(--white)}
.btn-dark{background:var(--ink);color:var(--white)}
.btn-ghost-dark{border:1px solid var(--ink);color:var(--ink)}
.eyebrow{position:absolute;font-size:9px;letter-spacing:1.6px;text-transform:uppercase;display:flex;align-items:center;gap:10px}
.eyebrow::after{content:"";width:44px;height:1px;background:currentColor;opacity:.7}
.dot{display:inline-block;width:10px;height:10px;border-radius:50%;background:var(--white);vertical-align:middle;margin-right:6px}
.nav{top:0;height:60px;z-index:5}
.brand{position:absolute;font-size:26px;font-weight:400;letter-spacing:-.3px;display:flex;align-items:center;gap:8px}
.brand i{width:14px;height:14px;background:var(--white);display:inline-block}
.menu{position:absolute;left:285px;top:24px;display:flex;gap:26px;font-size:11px}
.menu span::after{content:" ▾";font-size:8px}
.hero{top:0;height:562px;background:radial-gradient(ellipse at 20% 100%,#262626 0%,#050505 60%)}
.hero h1{position:absolute;left:110px;top:190px;font-size:40px;line-height:46px}
.hero p{position:absolute;left:112px;top:294px;width:420px;font-size:10.5px;line-height:15px;color:#ddd}
.plan{top:562px;height:150px;background:var(--white);color:var(--ink)}
.field{position:absolute;top:82px;height:32px;border:1px solid #bbb;font-size:10px;color:#999;padding:0 10px;display:flex;align-items:center;justify-content:space-between}
.featured{top:712px;height:161px;background:var(--band)}
.press{position:absolute;top:78px;font-size:19px;color:#7d7d7d;font-weight:500}
.features{top:873px;height:232px;background:linear-gradient(180deg,#181818,#0f0f0f)}
.feature{position:absolute;top:52px;width:270px}
.feature .ic{width:58px;height:58px;border-radius:50%;border:1px solid rgba(255,255,255,.4);background:#2a2a2a;display:flex;align-items:center;justify-content:center}
.feature h3{font-size:14px;font-weight:400;margin-top:27px}
.feature p{font-size:10px;color:#9a9a9a;line-height:15px;margin-top:12px}
.discover{top:1105px;height:535px;background:radial-gradient(ellipse at 70% 50%,#6b6b6b,#4a4a4a)}
.discover h2,.lux h2,.exp h2{position:absolute;font-size:32px;line-height:42px}
.body{position:absolute;font-size:10.5px;line-height:15px;color:#e6e6e6}
.lux{top:1640px;height:427px;background:var(--dark)}
.card{position:absolute;top:205px;height:161px;border:1px solid rgba(255,255,255,.45);padding:30px 28px}
.card h3{font-size:14px;font-weight:400;margin-top:18px}
.card p{font-size:10px;color:#8f8f8f;line-height:14px;margin-top:12px}
.cta{top:2067px;height:259px;background:linear-gradient(180deg,#ffffff 0%,#f2f3f5 55%,#b9bec4 100%);color:var(--ink);text-align:center}
.cta h2{position:absolute;left:0;width:1200px;top:66px;font-size:32px}
.exp{top:2326px;height:542px;background:linear-gradient(90deg,#4d4d4d,#6a6a6a)}
.faq{top:2868px;height:660px;background:linear-gradient(180deg,#1c1c1c,#141414)}
.q{position:absolute;left:590px;width:497px;height:40px;border:1px solid rgba(255,255,255,.5);font-size:11px;padding:0 24px;display:flex;align-items:center;justify-content:space-between}
.testi{top:3528px;height:430px;background:linear-gradient(180deg,#fff,#e9e9e9);color:var(--ink)}
.testi blockquote{position:absolute;left:110px;top:108px;width:500px;font-size:32px;font-weight:300;line-height:42px}
.trusted{top:3958px;height:194px;background:linear-gradient(180deg,#e9e9e9,#dcdcdc);color:var(--ink)}
.logo-box{position:absolute;top:72px;width:143px;height:67px;border:1px solid #999;background:#f7f7f7;display:flex;align-items:center;justify-content:center;font-size:18px;font-weight:500;color:#222}
.contact{top:4152px;height:420px;background:radial-gradient(ellipse at 50% 90%,#4a4540,#151515 70%)}
.input{position:absolute;height:32px;border:1px solid rgba(255,255,255,.45);font-size:9px;color:#aaa;padding:0 12px;display:flex;align-items:center}
.foot{top:4572px;height:428px;background:var(--black)}
.col{position:absolute;top:52px;font-size:9px;line-height:18px;color:#a9a9a9}
.col h4{font-size:12px;font-weight:500;color:var(--white);margin-bottom:8px}
.badge{position:absolute;top:310px;height:36px;background:#4a4a4a}
</style>
</head>
<body>

<section class="hero">
  <div class="photo" role="img" aria-label="Private jet nose on the tarmac at sunset" style="left:700px;top:120px;width:500px;height:442px;background:linear-gradient(180deg,#1b1b1b 0%,#2b2b2b 45%,#4a3c2c 80%,#6b5336 100%)"></div>
  <h1>Experience the Ultimate<br>in Luxury Jet Travel</h1>
  <p>Quorvel offers fractional jet ownership, jet card programs, private jet lease programs, all access programs, helicopter access programs, and by the seat charter flights. Discover the perfect flight program for your needs.</p>
  <div class="btn btn-light" style="left:112px;top:368px;width:118px">Explore</div>
  <div class="btn btn-ghost" style="left:238px;top:368px;width:128px">Learn More</div>
</section>

<header class="nav">
  <div class="brand" style="left:110px;top:14px">Quorvel <i></i></div>
  <nav class="menu"><span>Aircraft</span><span>Programs</span><span>Why Quorvel</span><span>Lifestyle</span><span>Sustainability</span><span>Resources</span><span>Competitors</span></nav>
  <div class="btn btn-ghost" style="left:953px;top:14px;width:134px;height:32px">Contact Us ➤</div>
</header>

<section class="plan">
  <div class="abs" style="left:112px;top:42px;font-size:17px">Plan A Flight</div>
  <div class="abs" style="left:288px;top:49px;font-size:9px"><span class="dot" style="background:var(--ink);width:8px;height:8px"></span>Round Trip &nbsp;&nbsp;&nbsp; <span class="dot" style="background:none;border:1px solid #999;width:8px;height:8px"></span>One Way</div>
  <div class="field" style="left:112px;width:165px">Departure Airport <span>✈</span></div>
  <div class="field" style="left:288px;width:165px">Arrival Airport <span>✈</span></div>
  <div class="field" style="left:465px;width:165px">Departure Date <span>▦</span></div>
  <div class="field" style="left:643px;width:165px">Return Date <span>▦</span></div>
  <div class="field" style="left:818px;width:90px">Pax <span>▾</span></div>
  <div class="btn btn-dark" style="left:920px;top:82px;width:128px;height:32px">Search</div>
</section>

<section class="featured">
  <div class="abs" style="left:0;width:1200px;top:36px;text-align:center;font-size:9px;letter-spacing:1.6px;color:#ccc">——————&nbsp; AS FEATURED IN &nbsp;——————</div>
  <div class="press" style="left:112px">Harbor Ledger</div>
  <div class="press" style="left:365px">The Meridian Post</div>
  <div class="press" style="left:595px">CodeWire</div>
  <div class="press" style="left:797px">Voltline</div>
  <div class="press" style="left:945px">Pitchmark</div>
</section>

<section class="features">
  <div class="feature" style="left:110px"><div class="ic"><svg width="26" height="26" viewBox="0 0 26 26" fill="none" stroke="#fff" stroke-width="1.3"><path d="M3 14h8l5-5h5"/><path d="M5 19h10l6-6"/></svg></div><h3>Flexible Ownership Options Available</h3><p>Choose from a variety of ownership programs and enjoy the freedom to fly on your own terms.</p></div>
  <div class="feature" style="left:468px"><div class="ic"><svg width="26" height="26" viewBox="0 0 26 26" fill="none" stroke="#fff" stroke-width="1.3"><circle cx="11" cy="8" r="4"/><path d="M4 21c0-4 3-7 7-7"/><rect x="14" y="15" width="9" height="6"/></svg></div><h3>Convenient Jet Card Programs</h3><p>Access a fleet of private jets with our exclusive jet card programs, offering flexibility and comfort.</p></div>
  <div class="feature" style="left:825px"><div class="ic"><svg width="26" height="26" viewBox="0 0 26 26" fill="none" stroke="#fff" stroke-width="1.3"><path d="M4 16l7-7 4 4 7-7"/><path d="M4 21l6-3 4 2 8-5"/></svg></div><h3>Flexible Lease Programs</h3><p>Experience the luxury of private jet travel without the commitment with our flexible lease programs.</p></div>
</section>

<section class="discover">
  <div class="photo" role="img" aria-label="Business traveller in a suit standing beside a private jet" style="left:112px;top:62px;width:298px;height:337px;background:linear-gradient(160deg,#d8dde2,#8e959c 50%,#2e3238)"></div>
  <div class="photo" role="img" aria-label="Black and white private jet parked on the runway" style="left:285px;top:247px;width:240px;height:223px;background:linear-gradient(180deg,#e4e4e4,#9a9a9a 55%,#3b3b3b);border:4px solid #fff"></div>
  <div class="eyebrow" style="left:590px;top:128px">Discover</div>
  <h2 style="left:588px;top:145px">Experience the Luxury of<br>Fractional Jet Ownership</h2>
  <p class="body" style="left:590px;top:234px;width:440px">With Quorvel's fractional jet ownership program, you can enjoy the benefits of private jet travel without the hassle and expense of owning a whole aircraft. Our program offers flexibility, convenience, and access to a fleet of luxurious jets, allowing you to travel in style and comfort.</p>
  <div class="abs" style="left:590px;top:322px;font-size:10.5px"><span class="dot"></span>Flexible Ownership Options &nbsp;&nbsp;<span class="dot"></span>Convenient Booking Process &nbsp;&nbsp;<span class="dot"></span>Luxurious Fleet of Jets</div>
  <div class="btn btn-light" style="left:590px;top:362px;width:118px">Learn More</div>
  <div class="btn btn-ghost" style="left:725px;top:362px;width:110px">Get Started</div>
</section>

<section class="lux">
  <div class="eyebrow" style="left:110px;top:64px">Luxury</div>
  <h2 style="left:110px;top:80px">Experience the Ultimate<br>in Private Jet Travel</h2>
  <p class="body" style="left:590px;top:66px;width:480px;color:#aaa">Quorvel offers a wide range of exclusive services to meet your private jet travel needs. From fractional jet ownership to on-demand charter flights, we provide the highest level of luxury and convenience.</p>
  <div class="btn btn-light" style="left:590px;top:122px;width:118px">Learn More</div>
  <div class="btn btn-ghost" style="left:725px;top:122px;width:110px">Get Started</div>
  <div class="card" style="left:110px;width:317px"><svg width="32" height="32" viewBox="0 0 32 32" fill="none" stroke="#fff" stroke-width="1.2"><path d="M4 28L28 4M28 4l-4 14M28 4L14 8M10 22l-4 2 2-4"/></svg><h3>Fractional Jet Ownership</h3><p>Enjoy the benefits of owning a private<br>jet without the hassles.</p></div>
  <div class="card" style="left:442px;width:316px"><svg width="32" height="32" viewBox="0 0 32 32" fill="none" stroke="#fff" stroke-width="1.2"><path d="M6 26L26 6M12 8l10 2M22 20l-2-10M6 26l6-2"/></svg><h3>On-Demand Charter</h3><p>Fly wherever and whenever you want with<br>our flexible charter options.</p></div>
  <div class="card" style="left:772px;width:315px"><svg width="32" height="32" viewBox="0 0 32 32" fill="none" stroke="#fff" stroke-width="1.2"><rect x="5" y="7" width="22" height="20"/><path d="M5 12h22M10 4v6M22 4v6M12 19l4-3 4 3"/></svg><h3>Private Jet Lease Programs</h3><p>Experience the freedom of having a private<br>jet at your disposal.</p></div>
</section>

<section class="cta" role="img" aria-label="Soft white clouds seen from above">
  <h2>Experience luxury travel like never before</h2>
  <p class="abs" style="left:0;width:1200px;top:115px;font-size:10.5px">Contact us today to book your exclusive jet experience</p>
  <div class="btn btn-dark" style="left:473px;top:151px;width:120px">Learn More</div>
  <div class="btn btn-ghost-dark" style="left:607px;top:151px;width:114px">Get Started</div>
</section>

<section class="exp">
  <div class="photo" role="img" aria-label="Private jet flying above the clouds" style="left:835px;top:0;width:365px;height:542px;background:linear-gradient(180deg,#d9dde1,#f2f3f4 45%,#b8bcc1)"></div>
  <div class="eyebrow" style="left:110px;top:76px">Experience</div>
  <h2 style="left:110px;top:94px">Unparalleled Luxury and<br>Convenience for Private Aviation</h2>
  <p class="body" style="left:110px;top:190px;width:450px">Discover the ultimate in luxury and convenience with Quorvel. Our exclusive private aviation solutions provide you with unparalleled access to the world of private jets, ensuring a seamless and extraordinary travel experience.</p>
  <div class="abs" style="left:110px;top:258px;font-size:13px"><span class="dot"></span>Convenience</div>
  <p class="body" style="left:130px;top:280px;width:200px;font-size:10px">Enjoy hassle-free travel with our flexible scheduling and personalized services.</p>
  <div class="abs" style="left:365px;top:258px;font-size:13px"><span class="dot"></span>Luxury</div>
  <p class="body" style="left:383px;top:280px;width:170px;font-size:10px">Indulge in the lavish amenities and exquisite interiors of our private jets.</p>
  <div class="btn btn-light" style="left:112px;top:354px;width:118px">Learn More</div>
  <div class="btn btn-ghost" style="left:246px;top:354px;width:110px">Get Started</div>
</section>

<section class="faq">
  <div class="photo" role="img" aria-label="Woman on the phone in a private jet cabin" style="left:112px;top:62px;width:408px;height:535px;background:linear-gradient(160deg,#e8e2d8,#b3a995 45%,#5d5548);border:3px solid #ddd"></div>
  <h2 class="abs" style="left:588px;top:60px;font-size:32px">Frequently Asked Questions</h2>
  <p class="abs" style="left:590px;top:114px;font-size:10px;color:#999">Find answers to common questions about Quorvel's services and programs.</p>
  <div class="q" style="top:152px">What is Quorvel? <span>+</span></div>
  <div class="abs" style="left:590px;top:207px;width:497px;height:115px;background:var(--white);color:var(--ink);padding:16px 24px">
    <div style="font-size:11px">How it works?</div>
    <p style="font-size:9.5px;line-height:13px;color:#444;margin-top:8px">Quorvel works by allowing customers to purchase fractional ownership of a private jet, join jet card programs for a set number of flight hours, lease a private jet for a specific period, or access our all access and helicopter programs. We also offer charter flights where customers can book individual seats on private jets.</p>
  </div>
  <div class="q" style="top:337px">Why choose Quorvel? <span>+</span></div>
  <div class="q" style="top:390px">How to book? <span>+</span></div>
  <div class="q" style="top:444px">What are the benefits? <span>+</span></div>
  <div class="abs" style="left:590px;top:505px;font-size:12px">Still have questions?</div>
  <div class="abs" style="left:590px;top:524px;font-size:10px;color:#999">Contact us for more information.</div>
  <div class="btn btn-light" style="left:590px;top:547px;width:118px">Learn More</div>
  <div class="btn btn-ghost" style="left:725px;top:547px;width:110px">Get Started</div>
</section>

<section class="testi">
  <blockquote>“Quorvel's services have exceeded my expectations. The convenience and luxury of flying with them is unmatched.”</blockquote>
  <div class="abs" style="left:110px;top:302px;color:#d4a017;font-size:18px;letter-spacing:8px">★★★★★</div>
  <div class="photo" role="img" aria-label="Businessman in sunglasses beside a jet engine" style="left:673px;top:62px;width:414px;height:330px;background:linear-gradient(160deg,#cfd3d7,#8d9297 50%,#3a3d41);border:3px solid #fff;box-shadow:0 0 0 1px #ccc"></div>
</section>

<section class="trusted">
  <div class="abs" style="left:0;width:1200px;top:24px;text-align:center;font-size:18px;font-weight:300">——— &nbsp;Trusted by top-tier companies around the globe&nbsp; ———</div>
  <div class="abs" style="left:100px;top:96px;font-size:16px">‹</div>
  <div class="logo-box" style="left:122px">Orchard</div>
  <div class="logo-box" style="left:284px">Parcelo</div>
  <div class="logo-box" style="left:447px">Tessellate</div>
  <div class="logo-box" style="left:609px">Kanoro</div>
  <div class="logo-box" style="left:771px">Sorvane</div>
  <div class="logo-box" style="left:933px">Velmora</div>
  <div class="abs" style="left:1090px;top:96px;font-size:16px">›</div>
</section>

<section class="contact">
  <div class="photo" role="img" aria-label="Private jet on the runway under a dusky sky" style="left:0;top:0;width:1200px;height:420px;background:radial-gradient(ellipse at 55% 85%,rgba(120,105,85,.55),rgba(20,20,20,0) 60%)"></div>
  <h2 class="abs" style="left:0;width:1200px;top:50px;text-align:center;font-size:32px">Experience luxury travel like never before</h2>
  <p class="abs" style="left:230px;width:740px;top:95px;text-align:center;font-size:10px;line-height:14px;color:#ddd">Discover the ultimate in private jet travel with Quorvel. Whether you're looking for fractional jet ownership, jet card programs, private jet lease programs, all access programs, helicopter access programs, or by the seat charter flights, we have the perfect solution for your needs.</p>
  <div class="abs" style="left:110px;top:160px;font-size:15px">Request Information ——————</div>
  <div class="input" style="left:112px;top:193px;width:212px">First Name</div>
  <div class="input" style="left:330px;top:193px;width:212px">Last Name</div>
  <div class="input" style="left:112px;top:232px;width:212px">Phone Number</div>
  <div class="input" style="left:330px;top:232px;width:212px">Email</div>
  <div class="input" style="left:112px;top:271px;width:430px;height:44px;align-items:flex-start;padding-top:8px">Comments</div>
  <div class="btn btn-light" style="left:112px;top:330px;width:118px;height:30px">Submit</div>
  <div class="abs" style="left:608px;top:160px;font-size:15px">Call Us ——————</div>
  <div class="abs" style="left:608px;top:203px;width:469px;height:120px;border:1px solid rgba(255,255,255,.5)">
    <div class="abs" style="left:30px;top:30px;font-size:20px;font-weight:300"><svg width="16" height="16" viewBox="0 0 24 24" fill="none" stroke="#fff" stroke-width="1.6" style="vertical-align:-2px"><path d="M5 3h4l2 5-3 2a12 12 0 006 6l2-3 5 2v4a2 2 0 01-2 2A18 18 0 013 5a2 2 0 012-2z"/></svg> +1.800.555.0147</div>
    <p class="abs" style="left:32px;top:68px;width:150px;font-size:9px;line-height:12px;color:#ccc">Call today for a personal consultation with one of our private aviation experts.</p>
    <div class="abs" style="left:255px;top:48px;width:22px;height:22px;border-radius:50%;border:1px solid #aaa;font-size:9px;display:flex;align-items:center;justify-content:center">or</div>
    <div class="btn btn-light" style="left:307px;top:44px;width:130px;height:30px">Schedule a Call</div>
  </div>
</section>

<footer class="foot">
  <div class="brand" style="left:110px;top:42px">Quorvel <i></i></div>
  <div class="abs" style="left:110px;top:92px;font-size:12px;font-weight:500">Follow Us:</div>
  <div class="abs" style="left:110px;top:114px;display:flex;gap:8px">
    <span style="width:24px;height:24px;border-radius:50%;border:1px solid #fff"></span><span style="width:24px;height:24px;border-radius:50%;border:1px solid #fff"></span><span style="width:24px;height:24px;border-radius:50%;border:1px solid #fff"></span><span style="width:24px;height:24px;border-radius:50%;border:1px solid #fff"></span><span style="width:24px;height:24px;border-radius:50%;border:1px solid #fff"></span>
  </div>
  <div class="abs" style="left:110px;top:154px;width:85px;height:26px;background:#fff;color:var(--ink);font-size:9px;font-weight:500;display:flex;align-items:center;justify-content:center">App Market</div>
  <div class="abs" style="left:202px;top:154px;width:85px;height:26px;background:#fff;color:var(--ink);font-size:9px;font-weight:500;display:flex;align-items:center;justify-content:center">Play Shelf</div>
  <div class="col" style="left:345px"><h4>About Us</h4>Pilots &amp; Crews<br>Safety<br>Aircraft Maintenance<br>Global Presence<br>Financial Strength<br>Personal Security<br>Private Terminals<br>Culture &amp; Heritage<br>Skyline Service</div>
  <div class="col" style="left:483px"><h4>Services</h4>Fractional Jet Ownership<br>Private Jet Lease<br>Jet Card Program<br>All Access<br>Helicopter Access<br>Single Seat Service<br>On-Demand Charter</div>
  <div class="col" style="left:633px"><h4>Company</h4>Terms<br>Privacy<br>Careers<br>Press<br>Blog<br>Contact</div>
  <div class="col" style="left:770px;width:320px"><h4>Subscribe to Our Newsletter</h4>Join our mailing list for the latest updates.</div>
  <div class="input" style="left:770px;top:100px;width:215px;height:32px">Enter Your Email</div>
  <div class="btn btn-light" style="left:990px;top:100px;width:97px;height:32px">Subscribe</div>
  <p class="abs" style="left:770px;top:142px;width:290px;font-size:9px;line-height:14px;color:#999">By subscribing, you agree to our Privacy Policy and consent to receive updates.</p>
  <div class="abs" style="left:110px;top:318px;font-size:13px">Awards &amp; Recognition</div>
  <div class="badge" style="left:348px;width:80px"></div>
  <div class="badge" style="left:475px;width:46px;border-radius:50%;height:46px;top:305px"></div>
  <div class="badge" style="left:565px;width:70px"></div>
  <div class="badge" style="left:688px;width:84px"></div>
  <div class="badge" style="left:838px;width:100px"></div>
  <div class="badge" style="left:978px;width:110px"></div>
  <div class="abs" style="left:110px;top:380px;width:977px;border-top:1px solid #333"></div>
  <div class="abs" style="left:0;width:1200px;top:396px;text-align:center;font-size:9px;color:#aaa">© 2024 Quorvel. All rights reserved. &nbsp;&nbsp;&nbsp;&nbsp; Privacy Policy &nbsp;&nbsp;&nbsp;&nbsp; Terms of Service &nbsp;&nbsp;&nbsp;&nbsp; Cookie Settings</div>
</footer>

</body>
</html>
```